Drug safety monitoring company requires a new corporate website

We are an outsourcing partner to large and small companies within the pharmaceutical industry. Our current website www.quorvanta.co.uk has not been updated in a long time. We want a new web site that is responsive and modern but with a clearly corporate and professional feel. We want a design based on a 12 column grid system (mobile and desktop version). We want to use a new, modern font (not the standard web fonts) - we will purchase as required. Content can be used as is from the current website. Red and white are the corporate colours, so a palate should be developed to match. We do not need as much red as is in the current website. New icons (preferably in svg format) would be great. We can also purchase new images from Framly (or other) as required. We would prefer submissions in Sketch if possible.

Target Market(s)

Pharmaceutical companies

Number of Pages Required

1 page

Font styles to use
Sans Serif

Colors
ec1f27
ffffff

Requirements
Must have
• Design based on 12 column grid system.
Responsive design (i.e. require a mobile and desktop version).
How should the menu look between desktop and mobile?
A coherent colour palete.
Content to come from the existing website: www.quorvanta.co.uk
How should links be styled?
How should headings, sub-headings, paragraphs be styled?
Nice to have
• Custom developed icons (these are along the bottom of the page on the existing website: Medical Information; Pharmacovigilance; Literature Monitoring; Training).
New imagery (the images on the current website are dated).
Submission ideally as Sketch files (but we are okay with photoshop too).
A new, modern, non-standard font.
Not so much red in the design.
If we had buttons on the website, how should they be styled?
If we had a form on the website, how should the fields be styled?

```html
<!DOCTYPE html>
<html lang="en">
<head>
<meta charset="utf-8">
<title>Quorvanta – Home Page Concepts</title>
<link href="https://fonts.googleapis.com/css2?family=Montserrat:wght@300;400;500;600;700&family=Poppins:wght@300;400;600;700&display=swap" rel="stylesheet">
<style>
:root{
  --red:#ec1f27;
  --white:#ffffff;
  --ink:#1c1c1c;
  --text:#3a3a3a;
  --bar:#2e2e2e;
  --soft:#f6f6f6;
}
*{margin:0;padding:0;box-sizing:border-box}
html,body{width:1200px;height:833px;overflow:hidden;background:var(--white)}
body{position:relative;font-family:"Montserrat",sans-serif;color:var(--text)}
.backdrop{position:absolute;left:0;top:0}
.brand{position:absolute;left:0;width:1200px;top:30px;display:flex;justify-content:center;align-items:center;gap:8px}
.brand-dot{width:14px;height:14px;border-radius:50%;background:var(--red)}
.brand-name{font-family:"Montserrat",sans-serif;font-weight:500;font-size:26px;letter-spacing:5px;color:var(--red)}
.page-title{position:absolute;top:76px;width:300px;text-align:center;font-family:"Poppins",sans-serif;font-weight:700;font-size:21px;color:var(--ink);letter-spacing:-.3px}
.page-title.first{left:172px}
.page-title.second{left:727px}

.site{position:absolute;top:120px;width:533px;height:660px;background:var(--white);box-shadow:0 2px 8px rgba(0,0,0,.12);overflow:hidden}
.site.first{left:56px}
.site.second{left:611px}
.site > *{position:absolute}

.topbar{left:0;top:0;width:533px;height:15px;background:var(--bar);color:var(--white);font-size:4.4px;font-weight:500}
.topbar span{position:absolute;top:0;line-height:15px;display:flex;align-items:center;gap:4px}
.topbar i{display:inline-block;width:8px;height:8px;border-radius:50%;background:var(--white);position:relative}
.topbar i::after{content:"";position:absolute;left:2.5px;top:2.5px;width:3px;height:3px;border-radius:1px;background:var(--red)}
.topbar .sep{position:absolute;top:4px;width:.6px;height:7px;background:#777}

.navbar{left:0;top:15px;width:533px;height:28px;background:var(--white)}
.logo-card{left:77px;top:15px;width:64px;height:37px;background:var(--white);box-shadow:0 1px 4px rgba(0,0,0,.14);z-index:3;display:flex;align-items:center;justify-content:center;font-weight:600;font-size:7px;letter-spacing:1px;color:var(--red)}
.nav{left:0;top:23px;width:533px;height:12px;z-index:3;font-size:4.6px;font-weight:500;color:var(--red)}
.nav a{position:absolute;top:0;line-height:12px;text-decoration:none;color:var(--red)}
.nav a.active{background:var(--red);color:var(--white);border-radius:6px;padding:0 6px;height:11px;line-height:11px}
.nav a.login{border:.7px solid var(--red);border-radius:6px;padding:0 6px;height:12px;line-height:11px;font-family:"Poppins",sans-serif;font-size:5px}

.hero-band{left:0;top:43px;width:533px;height:175px;background:linear-gradient(90deg,#f4f4f4,#ececec)}
.hero-photo{left:250px;top:43px;width:283px;height:175px}
.first .hero-photo{background:linear-gradient(90deg,#eeeeee 0%,#e2ded9 30%,#cfc8c1 55%,#a9bdd0 72%,#ddd7d1 100%)}
.second .hero-photo{background:linear-gradient(90deg,#eeeeee 0%,#e6e1da 30%,#d8c6b2 55%,#f1f1f1 72%,#d9dde0 100%)}
.hero-title{left:77px;top:96px;font-family:"Poppins",sans-serif;font-size:15px;line-height:18px;font-weight:300;color:var(--ink);letter-spacing:-.3px;white-space:nowrap;z-index:2}
.hero-title b{font-weight:700;color:var(--red)}
.hero-rule{left:77px;top:116px;width:22px;height:1.4px;background:var(--red)}
.hero-text{left:77px;top:121px;width:185px;font-size:6px;line-height:9px;color:var(--text)}
.hero-text em{color:var(--red)}
.btn{top:151px;height:16px;border-radius:8px;font-size:4.8px;font-weight:600;line-height:16px;text-align:center}
.btn.primary{left:77px;width:65px;background:var(--red);color:var(--white)}
.btn.ghost{left:148px;width:67px;background:var(--white);color:var(--red);box-shadow:0 1px 4px rgba(0,0,0,.12)}
.arrow{top:120px;width:20px;height:20px;border-radius:50%;background:var(--white);box-shadow:0 1px 3px rgba(0,0,0,.08)}
.arrow.prev{left:34px}
.arrow.next{left:479px}
.arrow svg{position:absolute;left:6px;top:6px}

.about-title{left:77px;top:242px;font-family:"Poppins",sans-serif;font-size:12.5px;font-weight:300;color:var(--ink)}
.about-title b{font-weight:700;color:var(--red)}
.about-intro{left:77px;top:268px;width:381px;font-size:4.9px;line-height:8.7px;text-align:justify}
.about-frame{left:77px;top:293px;width:153px;height:153px;background:var(--white);box-shadow:0 1px 5px rgba(0,0,0,.14)}
.about-photo{left:85px;top:302px;width:136px;height:135px;background:radial-gradient(circle at 55% 55%,#c9242b 0%,#a8414a 18%,#6b4a44 32%,#2a2a2a 60%,#1f1f1f 100%)}
.about-copy{left:239px;top:292px;width:218px;font-size:4.9px;line-height:8.7px;text-align:justify}
.about-copy p{margin-bottom:5px}

.services{left:0;top:471px;width:533px;height:143px;background:linear-gradient(100deg,#3b4a4f 0%,#43535a 60%,#4b5a60 100%)}
.service{top:499px;width:92px;text-align:center;color:var(--white)}
.service .icon{width:37px;height:37px;border-radius:50%;background:var(--white);margin:0 auto;display:flex;align-items:center;justify-content:center}
.service .icon span{display:block;width:20px;height:20px;border-radius:4px;background:linear-gradient(135deg,#5b8fd6,#ec1f27)}
.service h3{font-family:"Poppins",sans-serif;font-size:7px;font-weight:600;margin-top:7px;white-space:nowrap}
.service p{font-size:4.9px;line-height:8.7px;margin-top:2px;padding:0 3px;color:#e8ecee}
.svc-divider{top:506px;width:.6px;height:84px;background:rgba(255,255,255,.35)}

.footer{left:0;top:614px;width:533px;height:46px;background:var(--soft)}
.foot-item{top:628px;display:flex;align-items:center;gap:6px}
.foot-item .dot{width:14px;height:14px;border-radius:50%;background:var(--red);position:relative;flex:none}
.foot-item .dot svg{position:absolute;left:3.5px;top:3.5px}
.foot-item small{display:block;font-size:4.8px;font-weight:500;color:var(--ink)}
.foot-item strong{display:block;font-size:6.4px;font-weight:500;color:var(--ink)}
.foot-divider{top:625px;width:.6px;height:24px;background:var(--red)}
</style>
</head>
<body>

<svg class="backdrop" width="1200" height="833" viewBox="0 0 1200 833" aria-hidden="true">
  <polygon points="0,833 1200,833 1200,501 1118,780 800,780" fill="#ec1f27"/>
</svg>

<div class="brand"><span class="brand-dot"></span><span class="brand-name">QUORVANTA</span></div>
<div class="page-title first">HOME PAGE 1</div>
<div class="page-title second">HOME PAGE 2</div>

<section class="site first">
  <div class="topbar">
    <span style="left:81px"><i></i>Call Us : +44(0)330 7421 908</span>
    <b class="sep" style="left:190px"></b>
    <span style="left:224px"><i></i>Mail Us : admin@quorvanta.co.uk</span>
    <b class="sep" style="left:345px"></b>
    <span style="left:379px"><i></i>Fax Us : +44(0)870 5102 664</span>
  </div>
  <div class="navbar"></div>
  <div class="hero-band"></div>
  <div class="hero-photo" role="img" aria-label="Photo of a doctor's hand offering blister packs of tablets"></div>
  <div class="logo-card">QUORVANTA</div>
  <nav class="nav">
    <a class="active" style="left:182px">HOME</a>
    <a style="left:218px">ABOUT US</a>
    <a style="left:260px">QPPV</a>
    <a style="left:289px">OUR SERVICES ▾</a>
    <a style="left:347px">CONTACT US</a>
    <a class="login" style="left:399px">&#9711; | Client Login</a>
  </nav>
  <h1 class="hero-title">WELCOME <b>TO QUORVANTA</b></h1>
  <div class="hero-rule"></div>
  <p class="hero-text">At <em>Quorvanta</em> we ensure that your business has the best Pharmacovigilance support in the industry</p>
  <div class="btn primary">CONTACT NOW &nbsp;|&nbsp; ▣</div>
  <div class="btn ghost">GET BROCHURE &nbsp;|&nbsp; ⬇</div>
  <div class="arrow prev"><svg width="8" height="8" viewBox="0 0 8 8"><path d="M5.5 1 L2.5 4 L5.5 7" fill="none" stroke="#ec1f27" stroke-width="1"/></svg></div>
  <div class="arrow next"><svg width="8" height="8" viewBox="0 0 8 8"><path d="M2.5 1 L5.5 4 L2.5 7" fill="none" stroke="#ec1f27" stroke-width="1"/></svg></div>

  <h2 class="about-title">ABOUT <b>US</b></h2>
  <p class="about-intro">Welcome to the Quorvanta Pharmacovigilance website. We are an outsourcing partner to large and small companies within the pharmaceutical industry. Our range of services is tailored to suit each of our client’s needs and cover both human and veterinary medicinal products.</p>
  <div class="about-frame"></div>
  <div class="about-photo" role="img" aria-label="Photo of cupped hands holding a red fabric heart beside blister packs"></div>
  <div class="about-copy">
    <p>Pharmacovigilance is defined by WHO as ‘The science and activities relating to the detection, assessment, understanding and prevention of adverse effects or any other drug-related problems’. The process is one of managing risk associated with medicinal products, in an effort to promote their safe and effective use by prescribers and patients.</p>
    <p>Our primary functions are EU QPPV and related pharmacovigilance services to assist and support Marketing Authorisation Holders (MAH), of pharmaceutical product licences, in their efforts to remain compliant with EU regulatory requirements (Regulation 1235/2010 and Directive 2010/84/EU) the deadline for which implementing ended on 21 July 2012.</p>
    <p>The regulatory environment is an ever-changing and evolving one. Legislation is global and the management of this process is complex, requiring a strong relationship between Marketing Authorisation Holders and their QPPV.</p>
    <p>Good Pharmacovigilance Practice is dependant on a sound understanding of the key principles of this science and the ability to apply this knowledge competently on behalf of the client.</p>
  </div>

  <div class="services" role="img" aria-label="Dark teal photo of pills, syringes and a stethoscope"></div>
  <div class="service" style="left:74px"><div class="icon"><span role="img" aria-label="Medical information icon"></span></div><h3>Medical Information</h3><p>Professional enquiry handling to support the safe and effective use of your products.</p></div>
  <b class="svc-divider" style="left:170px"></b>
  <div class="service" style="left:172px"><div class="icon"><span role="img" aria-label="Heart with pulse icon"></span></div><h3>Pharmacovigilance</h3><p>Ease the regulatory burden and keep compliant with current pharmacovigilance legislation.</p></div>
  <b class="svc-divider" style="left:267px"></b>
  <div class="service" style="left:269px"><div class="icon"><span role="img" aria-label="Books and magnifier icon"></span></div><h3>Literature Monitoring</h3><p>Product safety through surveillance of published articles and case reports.</p></div>
  <b class="svc-divider" style="left:364px"></b>
  <div class="service" style="left:367px"><div class="icon"><span role="img" aria-label="Trainer with audience icon"></span></div><h3>Training</h3><p>Confident staff to support the pharmacovigilance process.</p></div>

  <div class="footer"></div>
  <div class="foot-item" style="left:77px"><span class="dot"><svg width="7" height="7" viewBox="0 0 10 10"><path d="M2 1 L4 1 L5 3.5 L3.8 4.5 Q5 6.5 5.5 6.2 L6.5 5 L9 6 L9 8 Q8 9.5 6 8.5 Q2 6.5 1 3 Q1 1.5 2 1Z" fill="#fff"/></svg></span><div><small>Contact Us On</small><strong>0330 7421 908</strong></div></div>
  <b class="foot-divider" style="left:170px"></b>
  <div class="foot-item" style="left:195px"><span class="dot"><svg width="7" height="7" viewBox="0 0 10 10"><path d="M4 2 H2 V8 H8 V6 M6 1 H9 V4 M9 1 L5 5" fill="none" stroke="#fff" stroke-width="1.2"/></svg></span><div><small>Our Platform</small><strong>VIGIL</strong></div></div>
  <b class="foot-divider" style="left:274px"></b>
  <div class="foot-item" style="left:299px"><span class="dot"><svg width="7" height="7" viewBox="0 0 10 10"><circle cx="5" cy="5" r="4" fill="none" stroke="#fff" stroke-width="1"/><path d="M6.4 3.6 A2 2 0 1 0 6.4 6.4" fill="none" stroke="#fff" stroke-width="1"/></svg></span><div><small>Copyright © 2020 Quorvanta Ltd</small><strong>(Registered in England &amp;Wales : 08264137)</strong></div></div>
</section>

<section class="site second">
  <div class="topbar">
    <span style="left:81px"><i></i>Call Us : +44(0)330 7421 908</span>
    <b class="sep" style="left:190px"></b>
    <span style="left:224px"><i></i>Mail Us : admin@quorvanta.co.uk</span>
    <b class="sep" style="left:345px"></b>
    <span style="left:379px"><i></i>Fax Us : +44(0)870 5102 664</span>
  </div>
  <div class="navbar"></div>
  <div class="hero-band"></div>
  <div class="hero-photo" role="img" aria-label="Photo of a smiling pharmacist in a white coat in a pharmacy"></div>
  <div class="logo-card">QUORVANTA</div>
  <nav class="nav">
    <a class="active" style="left:182px">HOME</a>
    <a style="left:218px">ABOUT US</a>
    <a style="left:260px">QPPV</a>
    <a style="left:289px">OUR SERVICES ▾</a>
    <a style="left:347px">CONTACT US</a>
    <a class="login" style="left:399px">&#9711; | Client Login</a>
  </nav>
  <h1 class="hero-title">WELCOME <b>TO QUORVANTA</b></h1>
  <div class="hero-rule"></div>
  <p class="hero-text">At <em>Quorvanta</em> we ensure that your business has the best Pharmacovigilance support in the industry</p>
  <div class="btn primary">CONTACT NOW &nbsp;|&nbsp; ▣</div>
  <div class="btn ghost">GET BROCHURE &nbsp;|&nbsp; ⬇</div>
  <div class="arrow prev"><svg width="8" height="8" viewBox="0 0 8 8"><path d="M5.5 1 L2.5 4 L5.5 7" fill="none" stroke="#ec1f27" stroke-width="1"/></svg></div>
  <div class="arrow next"><svg width="8" height="8" viewBox="0 0 8 8"><path d="M2.5 1 L5.5 4 L2.5 7" fill="none" stroke="#ec1f27" stroke-width="1"/></svg></div>

  <h2 class="about-title">ABOUT <b>US</b></h2>
  <p class="about-intro">Welcome to the Quorvanta Pharmacovigilance website. We are an outsourcing partner to large and small companies within the pharmaceutical industry. Our range of services is tailored to suit each of our client’s needs and cover both human and veterinary medicinal products.</p>
  <div class="about-frame"></div>
  <div class="about-photo" role="img" aria-label="Photo of cupped hands holding a red fabric heart beside blister packs"></div>
  <div class="about-copy">
    <p>Pharmacovigilance is defined by WHO as ‘The science and activities relating to the detection, assessment, understanding and prevention of adverse effects or any other drug-related problems’. The process is one of managing risk associated with medicinal products, in an effort to promote their safe and effective use by prescribers and patients.</p>
    <p>Our primary functions are EU QPPV and related pharmacovigilance services to assist and support Marketing Authorisation Holders (MAH), of pharmaceutical product licences, in their efforts to remain compliant with EU regulatory requirements (Regulation 1235/2010 and Directive 2010/84/EU) the deadline for which implementing ended on 21 July 2012.</p>
    <p>The regulatory environment is an ever-changing and evolving one. Legislation is global and the management of this process is complex, requiring a strong relationship between Marketing Authorisation Holders and their QPPV.</p>
    <p>Good Pharmacovigilance Practice is dependant on a sound understanding of the key principles of this science and the ability to apply this knowledge competently on behalf of the client.</p>
  </div>

  <div class="services" role="img" aria-label="Dark teal photo of pills, syringes and a stethoscope"></div>
  <div class="service" style="left:74px"><div class="icon"><span role="img" aria-label="Medical information icon"></span></div><h3>Medical Information</h3><p>Professional enquiry handling to support the safe and effective use of your products.</p></div>
  <b class="svc-divider" style="left:170px"></b>
  <div class="service" style="left:172px"><div class="icon"><span role="img" aria-label="Heart with pulse icon"></span></div><h3>Pharmacovigilance</h3><p>Ease the regulatory burden and keep compliant with current pharmacovigilance legislation.</p></div>
  <b class="svc-divider" style="left:267px"></b>
  <div class="service" style="left:269px"><div class="icon"><span role="img" aria-label="Books and magnifier icon"></span></div><h3>Literature Monitoring</h3><p>Product safety through surveillance of published articles and case reports.</p></div>
  <b class="svc-divider" style="left:364px"></b>
  <div class="service" style="left:367px"><div class="icon"><span role="img" aria-label="Trainer with audience icon"></span></div><h3>Training</h3><p>Confident staff to support the pharmacovigilance process.</p></div>

  <div class="footer"></div>
  <div class="foot-item" style="left:77px"><span class="dot"><svg width="7" height="7" viewBox="0 0 10 10"><path d="M2 1 L4 1 L5 3.5 L3.8 4.5 Q5 6.5 5.5 6.2 L6.5 5 L9 6 L9 8 Q8 9.5 6 8.5 Q2 6.5 1 3 Q1 1.5 2 1Z" fill="#fff"/></svg></span><div><small>Contact Us On</small><strong>0330 7421 908</strong></div></div>
  <b class="foot-divider" style="left:170px"></b>
  <div class="foot-item" style="left:195px"><span class="dot"><svg width="7" height="7" viewBox="0 0 10 10"><path d="M4 2 H2 V8 H8 V6 M6 1 H9 V4 M9 1 L5 5" fill="none" stroke="#fff" stroke-width="1.2"/></svg></span><div><small>Our Platform</small><strong>VIGIL</strong></div></div>
  <b class="foot-divider" style="left:274px"></b>
  <div class="foot-item" style="left:299px"><span class="dot"><svg width="7" height="7" viewBox="0 0 10 10"><circle cx="5" cy="5" r="4" fill="none" stroke="#fff" stroke-width="1"/><path d="M6.4 3.6 A2 2 0 1 0 6.4 6.4" fill="none" stroke="#fff" stroke-width="1"/></svg></span><div><small>Copyright © 2020 Quorvanta Ltd</small><strong>(Registered in England &amp;Wales : 08264137)</strong></div></div>
</section>

</body>
</html>
```